" Atendimento ao público com acesso a internet, e prestando todo tipo de serviços como: impressão, xerox, informática (venda de alguns produtos), e papelaria em geral. "

```html
<!DOCTYPE html>
<html lang="pt-BR">
<head>
<meta charset="utf-8">
<title>Conecta Mais — Assinatura de e-mail</title>
<link rel="stylesheet" href="https://fonts.googleapis.com/css2?family=Montserrat:wght@400;500;600;700&display=swap">
<style>
  :root {
    --backdrop: #e6e6e6;
    --blue-start: #22a3ea;
    --blue-end: #31c6d6;
    --blue-accent: #1d8fe0;
    --text-blue: #2a9fd8;
    --navy: #1c2b4a;
    --white: #ffffff;
  }
  * { margin: 0; padding: 0; box-sizing: border-box; }
  html, body {
    width: 1200px; height: 1200px; overflow: hidden;
    background: var(--backdrop);
    font-family: "Montserrat", sans-serif;
  }
  .signature {
    position: absolute; left: 113px; top: 449px;
    width: 974px; height: 240px;
    display: flex; background: var(--white);
  }
  .brand-panel {
    position: relative; width: 518px; height: 100%;
    background: linear-gradient(90deg, var(--blue-start), var(--blue-end));
    display: flex; flex-direction: column; align-items: center; justify-content: center;
    gap: 14px;
  }
  .brand-name {
    display: flex; align-items: center; gap: 14px;
    font-weight: 700; font-size: 44px; letter-spacing: -1px;
    color: var(--navy);
  }
  .brand-dot {
    width: 26px; height: 26px; border-radius: 50%; background: var(--white);
  }
  .brand-tagline {
    font-size: 11px; font-weight: 500; letter-spacing: 4px; color: var(--white);
  }
  .accent-bar {
    width: 10px; height: 200px; margin-top: 20px;
    background: var(--blue-accent);
  }
  .contact-panel {
    flex: 1; padding: 28px 0 0 38px; color: var(--text-blue);
  }
  .person-name { font-size: 27px; font-weight: 500; line-height: 1.1; }
  .person-role { font-size: 21px; font-weight: 400; margin-bottom: 10px; }
  .contact-list { list-style: none; }
  .contact-item {
    display: flex; align-items: center; gap: 10px;
    font-size: 18px; line-height: 29px;
  }
  .contact-item svg { width: 16px; height: 16px; fill: var(--text-blue); flex: none; }
  .plain-square { width: 15px; height: 15px; background: var(--text-blue); border-radius: 2px; flex: none; }
  .plain-circle { width: 15px; height: 15px; border: 2px solid var(--text-blue); border-radius: 50%; flex: none; }
</style>
</head>
<body>
  <section class="signature">
    <div class="brand-panel">
      <div class="brand-name"><span class="brand-dot"></span>ConectaMais</div>
      <div class="brand-tagline">INTERNET • PAPELARIA • INFORMÁTICA</div>
    </div>
    <div class="accent-bar"></div>
    <div class="contact-panel">
      <p class="person-name">Nome Completo</p>
      <p class="person-role">Cargo ou função</p>
      <ul class="contact-list">
        <li class="contact-item">
          <svg viewBox="0 0 16 16"><path d="M3.5 1 L6 1 L7 4.5 L5.2 5.8 C6 7.8 8.2 10 10.2 10.8 L11.5 9 L15 10 L15 12.5 C15 14 13.8 15 12.5 15 C6.5 14.5 1.5 9.5 1 3.5 C1 2.2 2 1 3.5 1 Z"/></svg>
          (00) 0000-0000
        </li>
        <li class="contact-item">
          <svg viewBox="0 0 16 16"><path d="M1 3 H15 V13 H1 Z M2 4 L8 8.5 L14 4 Z" fill-rule="evenodd"/></svg>
          seuemail@exemplo.com
        </li>
        <li class="contact-item">
          <svg viewBox="0 0 16 16"><circle cx="8" cy="8" r="6.5" fill="none" stroke="#2a9fd8" stroke-width="1.5"/><ellipse cx="8" cy="8" rx="2.8" ry="6.5" fill="none" stroke="#2a9fd8" stroke-width="1.2"/><path d="M1.5 8 H14.5" stroke="#2a9fd8" stroke-width="1.2"/></svg>
          www.seusite.com.br
        </li>
        <li class="contact-item"><span class="plain-square"></span>/seuperfil</li>
        <li class="contact-item"><span class="plain-circle"></span>@seuperfil</li>
      </ul>
    </div>
  </section>
</body>
</html>
```